Expanding Training Company needs a powerpoint template to deliver a consistent professional image

We want to start with a ppt template that is clean and flexible.
We are a small training organisation focusing on personal effectiveness, leadership, management and change. The MD is a New Zealander living in the United Kingdom and loves the idea of the clean green image that NZ has and wants the PowerPoint template to reflect that. We are pragmatic in what we do - everything comes back to performance improvement. Our clients are big players and our presentations need to be as clean, and as professional as theirs. We need a template that is versatile and can have their logos added as necessary.
Our training tends to be very current and as such we would like to use a lot of images and less words/bullets. We have company colours, logos and fonts that we are happy with and will continue to use.

Here are our company values to give you a sense of what we are about…

As a learning organisation we are always looking to continually improve and renew, our material, ideas, and methods, and are continually on the look out for new techniques, interventions and applications that provide measurable results to our clients.

We think life is about people and relationships, and we are prepared to walk away if people don't keep their word, are untrustworthy or lack integrity, as life is just too short to work with arses.
And because we are not arses we admit when we are wrong and make good on our commitments.

For our clients its all about performance and training is a performance enhancer, we aim to provide training excellence tin all its guises that delivers performance and happy clients.

We harness the value of the team, we believe in Interdependence.

We make life easier for our clients and each other.

Flexibility, innovation and future focus/vision are what our clients can count on us for.

Work is one of many of life's great facilitators, we recognise and value the others - its not just about work.

Industry/Entity Type

It Company

Font styles to use
Other font styles liked:
• Avenir Next

Colors
abd037
9bcb3c

Requirements
Must have
• A clean look with multiple options for inserting images, tables, videos, text boxes etc
• copyright information
Nice to have
• Slide masters

```html
<!DOCTYPE html>
<html lang="en">
<head>
<meta charset="utf-8">
<title>Slide Design Idea Part 01a</title>
<link rel="stylesheet" href="https://fonts.googleapis.com/css2?family=Open+Sans:wght@400;600;700;800&display=swap">
<style>
:root{
  --bg:#3a0f10;
  --head:#5c2324;
  --sheet:#ffffff;
  --slate:#50535f;
  --slate-dk:#3f414b;
  --green:#1f9a46;
  --lime:#8dc63f;
  --mint:#8ec39c;
  --orange:#e85b12;
  --pink:#f6b7b9;
  --blue:#2f7fa6;
  --muted:#8a8a8a;
  --rule:#cfcfcf;
}
*{box-sizing:border-box;margin:0;padding:0}
html,body{width:1200px;height:930px;overflow:hidden}
body{background:var(--bg);font-family:"Open Sans",Arial,sans-serif;position:relative}
.page-title{position:absolute;top:18px;left:0;width:1200px;text-align:center;font-weight:800;font-size:34px;color:var(--head);letter-spacing:.5px}
.sheet{position:absolute;left:13px;top:116px;width:1179px;height:728px;background:var(--sheet)}
.grid{position:absolute;left:17px;top:10px;display:grid;grid-template-columns:repeat(6,172px);column-gap:23.3px;grid-auto-rows:120px}
.slide-cell{position:relative;width:172px}
.thumb{position:relative;width:172px;height:96px;background:#fff;box-shadow:0 1px 3px rgba(0,0,0,.4);overflow:hidden}
.caption{text-align:center;font-size:8.5px;color:#222;margin-top:7px}
.a{position:absolute}
.t{position:absolute;top:8px;left:0;width:100%;text-align:center;font-size:7px;color:#8d8d8d;font-weight:600}
.tag{position:absolute;top:4px;left:4px;width:4px;height:4px;background:var(--orange)}
.mark{position:absolute;top:4px;right:5px;width:10px;height:10px;border-radius:50%;background:var(--green)}
.mint{background:var(--mint)}
.slate{background:var(--slate)}
.green{background:var(--green)}
.orange{background:var(--orange)}
.pink{background:var(--pink)}
.blue{background:var(--blue)}
.lines{background:repeating-linear-gradient(#cdcdcd 0 1px,transparent 1px 3px)}
.lines-w{background:repeating-linear-gradient(rgba(255,255,255,.75) 0 1px,transparent 1px 3px)}
.dot{position:absolute;width:8px;height:8px;border-radius:50%}
.dot::after{content:"";position:absolute;left:3px;top:3px;width:2px;height:2px;border-radius:50%;background:#fff}
.tiny{font-size:3px;color:#777;position:absolute;white-space:nowrap}
.tiny-w{font-size:3px;color:#fff;position:absolute;white-space:nowrap}
.cover-title{position:absolute;color:#fff;font-weight:700;white-space:nowrap}
.photo{position:absolute}
.brand{position:absolute;display:flex;align-items:center;gap:2px;font-size:6px;font-weight:600;color:var(--green)}
.brand i{display:block;width:6px;height:6px;border-radius:50%;background:var(--green)}
.bars{position:absolute;display:flex;align-items:flex-end;gap:1px}
.bars span{display:block;width:3px}
</style>
</head>
<body>
<h1 class="page-title">SIDE DESIGN IDEA ( Part - 01a)</h1>

<main class="sheet">
<div class="grid">

<!-- Row 1 -->
<figure class="slide-cell"><div class="thumb">
  <div class="a slate" style="left:0;top:0;width:172px;height:42px"></div>
  <div class="cover-title" style="top:10px;width:172px;text-align:center;font-size:7px">PRESENTATION TITLE</div>
  <div class="a" style="top:21px;width:172px;text-align:center;font-size:3.5px;color:#c8d94a;font-weight:700">PRESENTATION SUB TITLE</div>
  <div class="brand" style="left:100px;top:50px"><i></i>Fernleaf</div>
  <div class="a green" style="left:100px;top:60px;width:72px;height:1px"></div>
</div><figcaption class="caption">Slide1.JPG</figcaption></figure>

<figure class="slide-cell"><div class="thumb">
  <div class="brand" style="left:102px;top:6px"><i></i>Fernleaf</div>
  <div class="a green" style="left:100px;top:17px;width:72px;height:1px"></div>
  <div class="photo" role="img" aria-label="City skyline photograph" style="left:0;top:33px;width:172px;height:41px;background:linear-gradient(#6d7280,#4e535d 60%,#3c3f46)"></div>
  <div class="a" style="left:0;top:74px;width:172px;height:1px;background:#c0392b"></div>
  <div class="a" style="top:79px;width:172px;text-align:center;font-size:5px;color:#c0392b;font-weight:700">ENTER YOUR PRESENTATION TITLE</div>
</div><figcaption class="caption">Slide2.JPG</figcaption></figure>

<figure class="slide-cell"><div class="thumb">
  <div class="photo" role="img" aria-label="Harbour city skyline photograph" style="inset:0;background:linear-gradient(#9fb0c4,#5d6f86 55%,#2c3a4d)"></div>
  <div class="a" style="left:0;top:0;width:172px;height:20px;background:rgba(70,72,84,.9)"></div>
  <div class="cover-title" style="top:6px;width:172px;text-align:center;font-size:7px">ENTER YOUR PRESENTATION TITLE</div>
  <div class="a" style="left:60px;top:28px;width:52px;height:52px;border-radius:50%;background:#fff;display:flex;align-items:center;justify-content:center;font-size:8px;font-weight:700;color:var(--green)">Fernleaf</div>
</div><figcaption class="caption">Slide3.JPG</figcaption></figure>

<figure class="slide-cell"><div class="thumb">
  <div class="photo" role="img" aria-label="Muted grey cityscape photograph" style="inset:0;background:linear-gradient(#6a6e78,#545862 60%,#474a52)"></div>
  <div class="a" style="left:0;top:0;width:172px;height:20px;background:rgba(70,72,84,.9)"></div>
  <div class="cover-title" style="top:6px;width:172px;text-align:center;font-size:7px">ENTER YOUR PRESENTATION TITLE</div>
  <div class="a" style="left:60px;top:28px;width:52px;height:52px;border-radius:50%;background:#fff;display:flex;align-items:center;justify-content:center;font-size:8px;font-weight:700;color:var(--green)">Fernleaf</div>
</div><figcaption class="caption">Slide4.JPG</figcaption></figure>

<figure class="slide-cell"><div class="thumb">
  <div class="photo" role="img" aria-label="Green tinted city photograph" style="inset:0;background:linear-gradient(#3fb067,#219a4a 60%,#177a39)"></div>
  <div class="a" style="left:14px;top:16px;width:158px;height:20px;background:rgba(20,110,50,.85);clip-path:polygon(4% 0,100% 0,100% 100%,0 100%)"></div>
  <div class="a pink" style="left:8px;top:22px;width:10px;height:6px"></div>
  <div class="cover-title" style="left:44px;top:21px;font-size:7.5px">PRESENTATION TITLE</div>
  <div class="a" style="left:0;top:66px;width:75px;height:16px;border-radius:0 8px 8px 0;background:#fff"></div>
  <div class="brand" style="left:6px;top:69px"><i></i>Fernleaf</div>
</div><figcaption class="caption">Slide5.JPG</figcaption></figure>

<figure class="slide-cell"><div class="thumb">
  <div class="photo" role="img" aria-label="Harbour with tower photograph" style="inset:0;background:linear-gradient(#b9cde0,#7f9bb5 55%,#3d5d7a)"></div>
  <div class="a" style="left:0;top:0;width:125px;height:96px;background:rgba(196,125,40,.85);clip-path:polygon(0 0,100% 0,88% 100%,0 100%)"></div>
  <div class="cover-title" style="left:32px;top:16px;font-size:7px">Title Slide</div>
  <div class="tiny-w" style="left:7px;top:30px">Sub Heading</div>
  <div class="a lines-w" style="left:7px;top:38px;width:100px;height:12px"></div>
  <div class="a lines-w" style="left:7px;top:64px;width:95px;height:9px"></div>
</div><figcaption class="caption">Slide6.JPG</figcaption></figure>

<!-- Row 2 -->
<figure class="slide-cell"><div class="thumb">
  <div class="tag"></div><div class="mark"></div>
  <div class="a slate" style="left:0;top:14px;width:57px;height:72px"></div>
  <div class="cover-title" style="left:5px;top:20px;font-size:6.5px">Title Slide</div>
  <div class="tiny-w" style="left:6px;top:31px">Sub Heading</div>
  <div class="a lines-w" style="left:6px;top:40px;width:44px;height:12px"></div>
  <div class="photo" role="img" aria-label="Cable car on a hillside photograph" style="left:62px;top:16px;width:93px;height:68px;background:linear-gradient(#9cc5e6,#6f9a5a 55%,#b33a3a 75%,#556b3c)"></div>
</div><figcaption class="caption">Slide7.JPG</figcaption></figure>

<figure class="slide-cell"><div class="thumb">
  <div class="tag"></div><div class="mark"></div>
  <div class="photo" role="img" aria-label="Dramatic landscape at dusk photograph" style="left:0;top:14px;width:172px;height:70px;background:linear-gradient(90deg,#4a3a3c,#7a4a48 45%,#5a2e2c)"></div>
  <div class="a slate" style="left:82px;top:14px;width:90px;height:70px;clip-path:polygon(14% 0,100% 0,100% 100%,0 100%)"></div>
  <div class="cover-title" style="left:100px;top:20px;font-size:6.5px">Title Slide</div>
  <div class="tiny-w" style="left:100px;top:31px">Sub Heading</div>
  <div class="a lines-w" style="left:100px;top:40px;width:64px;height:12px"></div>
</div><figcaption class="caption">Slide8.JPG</figcaption></figure>

<figure class="slide-cell"><div class="thumb">
  <div class="tag"></div><div class="mark"></div>
  <div class="photo" role="img" aria-label="City waterfront photograph" style="left:8px;top:14px;width:76px;height:68px;background:linear-gradient(#c9cfd6,#9aa3ae 55%,#6d737c)"></div>
  <div class="a" style="left:64px;top:14px;width:94px;height:68px;background:#f4f4f4;clip-path:polygon(22% 0,100% 0,100% 100%,0 100%)"></div>
  <div class="a orange" style="left:64px;top:30px;width:12px;height:14px;transform:skewX(-20deg);opacity:.85"></div>
  <div class="a orange" style="left:72px;top:50px;width:12px;height:14px;transform:skewX(-20deg);opacity:.85"></div>
  <div class="a" style="left:100px;top:20px;font-size:6.5px;color:#888;font-weight:600">Title Slide</div>
  <div class="tiny" style="left:100px;top:31px">Sub Heading</div>
  <div class="a lines" style="left:100px;top:40px;width:52px;height:12px"></div>
</div><figcaption class="caption">Slide9.JPG</figcaption></figure>

<figure class="slide-cell"><div class="thumb">
  <div class="photo" role="img" aria-label="Overcast skyline photograph" style="inset:0;background:linear-gradient(#7f838c,#5e626b 55%,#8d8f8f 80%,#55585e)"></div>
  <div class="a" style="left:0;top:22px;width:172px;height:46px;background:rgba(80,83,95,.85)"></div>
  <div class="cover-title" style="left:26px;top:27px;font-size:6.5px">Title Slide</div>
  <div class="tiny-w" style="left:26px;top:38px">Sub Heading</div>
  <div class="a lines-w" style="left:26px;top:46px;width:120px;height:9px"></div>
</div><figcaption class="caption">Slide10.JPG</figcaption></figure>

<figure class="slide-cell"><div class="thumb">
  <div class="tag"></div><div class="mark"></div><div class="t">About Us</div>
  <div class="a mint" style="left:8px;top:22px;width:54px;height:56px"></div>
  <div class="dot slate" style="left:90px;top:22px"></div>
  <div class="dot green" style="left:135px;top:22px"></div>
  <div class="dot" style="left:90px;top:50px;background:var(--lime)"></div>
  <div class="dot pink" style="left:135px;top:50px"></div>
  <div class="a lines" style="left:80px;top:36px;width:28px;height:7px"></div>
  <div class="a lines" style="left:125px;top:36px;width:28px;height:7px"></div>
  <div class="a lines" style="left:80px;top:64px;width:28px;height:7px"></div>
  <div class="a lines" style="left:125px;top:64px;width:28px;height:7px"></div>
</div><figcaption class="caption">Slide11.JPG</figcaption></figure>

<figure class="slide-cell"><div class="thumb">
  <div class="tag"></div><div class="mark"></div><div class="t">Our Team</div>
  <div class="a slate" style="left:0;top:54px;width:172px;height:26px"></div>
  <div class="a mint" style="left:10px;top:22px;width:46px;height:32px"></div>
  <div class="a mint" style="left:63px;top:22px;width:46px;height:32px"></div>
  <div class="a mint" style="left:116px;top:22px;width:46px;height:32px"></div>
  <div class="tiny-w" style="left:24px;top:56px">Jo Hart</div>
  <div class="tiny-w" style="left:76px;top:56px">Sam Lee</div>
  <div class="tiny-w" style="left:128px;top:56px">Ana Park</div>
  <div class="a lines-w" style="left:12px;top:64px;width:150px;height:7px"></div>
</div><figcaption class="caption">Slide12.JPG</figcaption></figure>

<!-- Row 3 -->
<figure class="slide-cell"><div class="thumb">
  <div class="tag"></div><div class="mark"></div><div class="t">Our Philosophy</div>
  <div class="dot green" style="left:36px;top:28px"></div>
  <div class="dot" style="left:82px;top:28px;background:var(--lime)"></div>
  <div class="dot orange" style="left:128px;top:28px"></div>
  <div class="dot slate" style="left:36px;top:60px"></div>
  <div class="dot slate" style="left:82px;top:60px"></div>
  <div class="dot green" style="left:128px;top:60px"></div>
  <div class="a lines" style="left:24px;top:40px;width:130px;height:7px"></div>
  <div class="a lines" style="left:24px;top:72px;width:130px;height:7px"></div>
</div><figcaption class="caption">Slide13.JPG</figcaption></figure>

<figure class="slide-cell"><div class="thumb">
  <div class="tag"></div><div class="mark"></div><div class="t">Bullet Style - 01</div>
  <div class="a mint" style="left:14px;top:26px;width:66px;height:56px"></div>
  <div class="a" style="left:94px;top:26px;font-size:3.5px;font-weight:700;color:#555">Sub Heading</div>
  <div class="a lines" style="left:94px;top:32px;width:68px;height:50px"></div>
</div><figcaption class="caption">Slide14.JPG</figcaption></figure>

<figure class="slide-cell"><div class="thumb">
  <div class="tag"></div><div class="mark"></div><div class="t">Bullet Style - 02</div>
  <div class="a" style="left:14px;top:22px;font-size:3.5px;font-weight:700;color:#555">List Style Written</div>
  <div class="a lines" style="left:14px;top:28px;width:150px;height:8px"></div>
  <div class="a lines" style="left:24px;top:40px;width:130px;height:44px"></div>
</div><figcaption class="caption">Slide15.JPG</figcaption></figure>

<figure class="slide-cell"><div class="thumb">
  <div class="tag"></div><div class="mark"></div><div class="t">Individual Skill</div>
  <div class="a mint" style="left:14px;top:26px;width:58px;height:56px"></div>
  <div class="a" style="left:78px;top:26px;font-size:3.5px;font-weight:700;color:#555">Person Name</div>
  <div class="a lines" style="left:78px;top:31px;width:80px;height:4px"></div>
  <svg class="a" style="left:78px;top:38px" width="90" height="44" viewBox="0 0 90 44" aria-hidden="true">
    <g fill="#ccc"><rect x="0" y="1" width="14" height="1"/><rect x="0" y="11" width="14" height="1"/><rect x="0" y="21" width="14" height="1"/><rect x="0" y="31" width="14" height="1"/></g>
    <g fill="#e85b12"><circle cx="20" cy="2" r="2.5"/><circle cx="26" cy="2" r="2.5"/><circle cx="32" cy="2" r="2.5"/><circle cx="38" cy="2" r="2.5"/><circle cx="44" cy="2" r="2.5"/><circle cx="50" cy="2" r="2.5"/></g>
    <g fill="#e8b012"><circle cx="20" cy="12" r="2.5"/><circle cx="26" cy="12" r="2.5"/><circle cx="32" cy="12" r="2.5"/><circle cx="38" cy="12" r="2.5"/><circle cx="44" cy="12" r="2.5"/></g>
    <g fill="#8dc63f"><circle cx="20" cy="22" r="2.5"/><circle cx="26" cy="22" r="2.5"/><circle cx="32" cy="22" r="2.5"/><circle cx="38" cy="22" r="2.5"/><circle cx="44" cy="22" r="2.5"/><circle cx="50" cy="22" r="2.5"/><circle cx="56" cy="22" r="2.5"/></g>
    <g fill="#2f7fa6"><circle cx="20" cy="32" r="2.5"/><circle cx="26" cy="32" r="2.5"/><circle cx="32" cy="32" r="2.5"/><circle cx="38" cy="32" r="2.5"/><circle cx="44" cy="32" r="2.5"/><circle cx="50" cy="32" r="2.5"/><circle cx="56" cy="32" r="2.5"/><circle cx="62" cy="32" r="2.5"/></g>
    <g fill="#ddd"><circle cx="56" cy="2" r="2.5"/><circle cx="62" cy="2" r="2.5"/><circle cx="50" cy="12" r="2.5"/><circle cx="56" cy="12" r="2.5"/><circle cx="62" cy="12" r="2.5"/><circle cx="62" cy="22" r="2.5"/></g>
  </svg>
</div><figcaption class="caption">Slide16.JPG</figcaption></figure>

<figure class="slide-cell"><div class="thumb">
  <div class="tag"></div><div class="mark"></div><div class="t">Personality</div>
  <div class="a mint" style="left:66px;top:22px;width:40px;height:56px"></div>
  <div class="dot" style="left:54px;top:28px;background:var(--lime)"></div>
  <div class="dot slate" style="left:54px;top:44px"></div>
  <div class="dot orange" style="left:54px;top:60px"></div>
  <div class="dot green" style="left:110px;top:28px"></div>
  <div class="dot slate" style="left:110px;top:44px"></div>
  <div class="dot orange" style="left:110px;top:60px"></div>
  <div class="a lines" style="left:10px;top:28px;width:40px;height:40px"></div>
  <div class="a lines" style="left:122px;top:28px;width:40px;height:40px"></div>
</div><figcaption class="caption">Slide17.JPG</figcaption></figure>

<figure class="slide-cell"><div class="thumb">
  <div class="tag"></div><div class="mark"></div><div class="t">Development</div>
  <div class="a mint" style="left:66px;top:20px;width:38px;height:54px"></div>
  <div class="dot green" style="left:56px;top:26px"></div>
  <div class="dot green" style="left:56px;top:52px"></div>
  <div class="dot slate" style="left:110px;top:26px"></div>
  <div class="dot slate" style="left:110px;top:52px"></div>
  <div class="a lines" style="left:10px;top:28px;width:40px;height:36px"></div>
  <div class="a lines" style="left:122px;top:28px;width:40px;height:36px"></div>
  <div class="a green" style="left:0;top:72px;width:172px;height:24px"></div>
  <div class="a lines-w" style="left:10px;top:77px;width:152px;height:8px"></div>
</div><figcaption class="caption">Slide18.JPG</figcaption></figure>

<!-- Row 4 -->
<figure class="slide-cell"><div class="thumb">
  <div class="tag"></div><div class="mark"></div><div class="t">Portfolio</div>
  <div class="a mint" style="left:8px;top:24px;width:36px;height:32px"></div>
  <div class="a mint" style="left:48px;top:24px;width:36px;height:32px"></div>
  <div class="a mint" style="left:88px;top:24px;width:36px;height:32px"></div>
  <div class="a mint" style="left:128px;top:24px;width:36px;height:32px"></div>
  <div class="a pink" style="left:8px;top:56px;width:36px;height:4px"></div>
  <div class="a" style="left:48px;top:56px;width:36px;height:4px;background:var(--lime)"></div>
  <div class="a" style="left:88px;top:56px;width:36px;height:4px;background:var(--lime)"></div>
  <div class="a green" style="left:128px;top:56px;width:36px;height:4px"></div>
  <div class="a lines" style="left:10px;top:64px;width:152px;height:14px"></div>
</div><figcaption class="caption">Slide19.JPG</figcaption></figure>

<figure class="slide-cell"><div class="thumb">
  <div class="tag"></div><div class="mark"></div><div class="t">Our Capabilities</div>
  <svg class="a" style="left:0;top:20px" width="172" height="34" viewBox="0 0 172 34" aria-hidden="true">
    <g fill="#8ec39c" stroke="#3f414b" stroke-width="1.5"><rect x="18" y="3" width="34" height="22"/><rect x="69" y="3" width="34" height="22"/><rect x="120" y="3" width="34" height="22"/></g>
    <g fill="#3f414b"><rect x="13" y="25" width="44" height="2"/><rect x="64" y="25" width="44" height="2"/><rect x="115" y="25" width="44" height="2"/></g>
  </svg>
  <div class="a green" style="left:0;top:53px;width:172px;height:9px"></div>
  <div class="tiny-w" style="left:26px;top:55px;font-weight:700">TITLE - 01</div>
  <div class="tiny-w" style="left:78px;top:55px;font-weight:700">TITLE - 01</div>
  <div class="tiny-w" style="left:128px;top:55px;font-weight:700">TITLE - 01</div>
  <div class="a lines" style="left:14px;top:66px;width:146px;height:12px"></div>
</div><figcaption class="caption">Slide20.JPG</figcaption></figure>

<figure class="slide-cell"><div class="thumb">
  <div class="tag"></div><div class="mark"></div><div class="t">Portfolio</div>
  <div class="a slate" style="left:0;top:40px;width:172px;height:56px"></div>
  <div class="a mint" style="left:14px;top:26px;width:30px;height:28px"></div>
  <div class="a mint" style="left:52px;top:26px;width:30px;height:28px"></div>
  <div class="a mint" style="left:90px;top:26px;width:30px;height:28px"></div>
  <div class="a mint" style="left:128px;top:26px;width:30px;height:28px"></div>
  <div class="tiny-w" style="left:14px;top:58px">TITLE - 01</div>
  <div class="tiny-w" style="left:52px;top:58px">TITLE - 01</div>
  <div class="tiny-w" style="left:90px;top:58px">TITLE - 01</div>
  <div class="tiny-w" style="left:128px;top:58px">TITLE - 01</div>
  <div class="a lines-w" style="left:14px;top:66px;width:144px;height:12px;opacity:.5"></div>
</div><figcaption class="caption">Slide21.JPG</figcaption></figure>

<figure class="slide-cell"><div class="thumb">
  <div class="tag"></div><div class="mark"></div><div class="t">Portfolio</div>
  <div class="a mint" style="left:14px;top:22px;width:34px;height:20px"></div>
  <div class="a mint" style="left:52px;top:22px;width:34px;height:20px"></div>
  <div class="a mint" style="left:90px;top:22px;width:34px;height:20px"></div>
  <div class="a mint" style="left:128px;top:22px;width:34px;height:20px"></div>
  <div class="a lines" style="left:14px;top:44px;width:148px;height:6px"></div>
  <div class="a mint" style="left:14px;top:54px;width:34px;height:20px"></div>
  <div class="a mint" style="left:52px;top:54px;width:34px;height:20px"></div>
  <div class="a mint" style="left:90px;top:54px;width:34px;height:20px"></div>
  <div class="a mint" style="left:128px;top:54px;width:34px;height:20px"></div>
  <div class="a lines" style="left:14px;top:76px;width:148px;height:6px"></div>
</div><figcaption class="caption">Slide22.JPG</figcaption></figure>

<figure class="slide-cell"><div class="thumb">
  <div class="tag"></div><div class="mark"></div><div class="t">Portfolio</div>
  <div class="a mint" style="left:0;top:22px;width:172px;height:58px"></div>
  <div class="a green" style="left:22px;top:22px;width:36px;height:28px"></div>
  <div class="a slate-dk" style="left:0;top:50px;width:22px;height:30px;background:var(--slate-dk)"></div>
  <div class="a" style="left:58px;top:50px;width:36px;height:30px;background:var(--lime)"></div>
  <div class="a" style="left:105px;top:22px;width:36px;height:28px;background:var(--slate-dk)"></div>
  <div class="a pink" style="left:141px;top:50px;width:31px;height:30px"></div>
  <div class="tiny-w" style="left:28px;top:25px">Portfolio 1</div>
  <div class="tiny-w" style="left:111px;top:25px">Portfolio 1</div>
</div><figcaption class="caption">Slide23.JPG</figcaption></figure>

<figure class="slide-cell"><div class="thumb">
  <div class="tag"></div><div class="mark"></div><div class="t">Slide Design Idea</div>
  <div class="a green" style="left:50px;top:24px;width:72px;height:16px"></div>
  <div class="a slate" style="left:50px;top:43px;width:72px;height:16px"></div>
  <div class="a orange" style="left:50px;top:62px;width:72px;height:16px"></div>
  <div class="a lines-w" style="left:68px;top:28px;width:50px;height:8px"></div>
  <div class="a lines-w" style="left:68px;top:47px;width:50px;height:8px"></div>
  <div class="a lines-w" style="left:68px;top:66px;width:50px;height:8px"></div>
  <div class="a" style="left:19px;top:36px;width:12px;height:12px;border-radius:50%;border:1px solid var(--green)"></div>
  <div class="a" style="left:141px;top:36px;width:12px;height:12px;border-radius:50%;border:1px solid var(--green)"></div>
  <div class="a lines" style="left:8px;top:54px;width:34px;height:10px"></div>
  <div class="a lines" style="left:130px;top:54px;width:34px;height:10px"></div>
</div><figcaption class="caption">Slide24.JPG</figcaption></figure>

<!-- Row 5 -->
<figure class="slide-cell"><div class="thumb">
  <div class="tag"></div><div class="mark"></div><div class="t">Slide Design Idea</div>
  <div class="a green" style="left:0;top:22px;width:35px;height:30px"></div>
  <div class="a" style="left:35px;top:22px;width:35px;height:30px;background:var(--lime)"></div>
  <div class="a slate" style="left:70px;top:22px;width:34px;height:30px"></div>
  <div class="a pink" style="left:104px;top:22px;width:34px;height:30px"></div>
  <div class="a" style="left:138px;top:22px;width:34px;height:30px;background:#777a84"></div>
  <div class="a" style="left:12px;top:32px;width:10px;height:10px;border-radius:50%;border:1.5px solid #fff"></div>
  <div class="a" style="left:47px;top:33px;width:11px;height:8px;border:1.5px solid #fff"></div>
  <div class="a" style="left:82px;top:32px;width:10px;height:10px;background:#fff;clip-path:polygon(50% 0,100% 100%,0 100%)"></div>
  <div class="a" style="left:116px;top:32px;width:10px;height:10px;border-radius:50%;background:#fff"></div>
  <div class="a" style="left:151px;top:32px;width:8px;height:10px;border:1.5px solid #fff"></div>
  <div class="a lines" style="left:6px;top:56px;width:160px;height:20px"></div>
</div><figcaption class="caption">Slide25.JPG</figcaption></figure>

<figure class="slide-cell"><div class="thumb">
  <div class="tag"></div><div class="mark"></div><div class="t">Slide Design Idea</div>
  <div class="a slate" style="left:10px;top:22px;width:68px;height:34px"></div>
  <div class="a pink" style="left:78px;top:22px;width:84px;height:34px"></div>
  <div class="tiny-w" style="left:66px;top:26px;font-weight:700">Title 01</div>
  <div class="a lines-w" style="left:30px;top:32px;width:78px;height:14px"></div>
  <div class="a orange" style="left:22px;top:62px;width:8px;height:7px"></div>
  <div class="a" style="left:62px;top:62px;width:8px;height:7px;background:var(--lime)"></div>
  <div class="a green" style="left:102px;top:62px;width:8px;height:7px"></div>
  <div class="a slate" style="left:142px;top:62px;width:8px;height:7px"></div>
  <div class="a lines" style="left:10px;top:72px;width:152px;height:10px"></div>
</div><figcaption class="caption">Slide26.JPG</figcaption></figure>

<figure class="slide-cell"><div class="thumb">
  <div class="tag"></div><div class="mark"></div><div class="t">Portfolio</div>
  <div class="a mint" style="left:12px;top:22px;width:148px;height:64px"></div>
  <div class="a green" style="left:48px;top:22px;width:48px;height:32px"></div>
  <div class="a slate" style="left:144px;top:22px;width:16px;height:32px;left:136px;width:24px"></div>
  <div class="a green" style="left:12px;top:54px;width:36px;height:32px"></div>
  <div class="a orange" style="left:96px;top:54px;width:40px;height:32px"></div>
  <div class="a lines-w" style="left:52px;top:28px;width:40px;height:20px"></div>
  <div class="a lines-w" style="left:100px;top:60px;width:32px;height:20px"></div>
</div><figcaption class="caption">Slide27.JPG</figcaption></figure>

<figure class="slide-cell"><div class="thumb">
  <div class="tag"></div><div class="mark"></div><div class="t">Portfolio</div>
  <div class="a mint" style="left:12px;top:24px;width:88px;height:58px"></div>
  <div class="a orange" style="left:100px;top:24px;width:34px;height:30px"></div>
  <div class="a green" style="left:134px;top:24px;width:28px;height:30px"></div>
  <div class="a green" style="left:100px;top:54px;width:34px;height:28px"></div>
  <div class="a slate" style="left:134px;top:54px;width:28px;height:28px"></div>
  <div class="a lines-w" style="left:104px;top:30px;width:26px;height:18px"></div>
  <div class="a lines-w" style="left:137px;top:30px;width:22px;height:18px"></div>
  <div class="a lines-w" style="left:104px;top:60px;width:26px;height:16px"></div>
  <div class="a lines-w" style="left:137px;top:60px;width:22px;height:16px"></div>
</div><figcaption class="caption">Slide28.JPG</figcaption></figure>

<figure class="slide-cell"><div class="thumb">
  <div class="tag"></div><div class="mark"></div><div class="t">Slide Design Idea</div>
  <div class="a orange" style="left:12px;top:24px;width:86px;height:30px"></div>
  <div class="a orange" style="left:100px;top:24px;width:32px;height:30px"></div>
  <div class="a blue" style="left:134px;top:24px;width:28px;height:58px"></div>
  <div class="a slate" style="left:12px;top:56px;width:32px;height:26px"></div>
  <div class="a slate" style="left:46px;top:56px;width:86px;height:26px"></div>
  <div class="a" style="left:110px;top:33px;width:12px;height:12px;border-radius:50%;border:1.5px solid #fff"></div>
  <div class="a" style="left:143px;top:34px;width:9px;height:12px;border:1.5px solid #fff;border-radius:2px"></div>
  <div class="a" style="left:22px;top:64px;width:12px;height:8px;background:#fff;border-radius:2px"></div>
  <div class="a lines-w" style="left:16px;top:32px;width:60px;height:8px"></div>
  <div class="a lines-w" style="left:60px;top:64px;width:60px;height:8px"></div>
</div><figcaption class="caption">Slide29.JPG</figcaption></figure>

<figure class="slide-cell"><div class="thumb">
  <div class="tag"></div><div class="mark"></div><div class="t">4 Point Design</div>
  <svg class="a" style="left:62px;top:24px" width="50" height="62" viewBox="0 0 50 62" aria-hidden="true">
    <polygon points="0,44 25,52 50,44 50,54 25,62 0,54" fill="#f6b7b9"/>
    <polygon points="0,30 25,38 50,30 50,42 25,50 0,42" fill="#555a62"/>
    <polygon points="0,16 25,24 50,16 50,28 25,36 0,28" fill="#8dc63f"/>
    <polygon points="0,8 25,0 50,8 50,14 25,22 0,14" fill="#1f9a46"/>
  </svg>
  <div class="a" style="left:10px;top:26px;width:40px;height:18px;border:1px solid var(--mint)"></div>
  <div class="a" style="left:10px;top:52px;width:40px;height:18px;border:1px solid var(--mint)"></div>
  <div class="a" style="left:122px;top:36px;width:40px;height:18px;border:1px solid var(--mint)"></div>
  <div class="a" style="left:122px;top:62px;width:40px;height:18px;border:1px solid var(--mint)"></div>
  <div class="a lines" style="left:14px;top:31px;width:32px;height:9px"></div>
  <div class="a lines" style="left:14px;top:57px;width:32px;height:9px"></div>
  <div class="a lines" style="left:126px;top:41px;width:32px;height:9px"></div>
  <div class="a lines" style="left:126px;top:67px;width:32px;height:9px"></div>
</div><figcaption class="caption">Slide30.JPG</figcaption></figure>

<!-- Row 6 -->
<figure class="slide-cell"><div class="thumb">
  <div class="tag"></div><div class="mark"></div><div class="t">4 Point Design</div>
  <div class="a mint" style="left:0;top:22px;width:88px;height:58px"></div>
  <div class="a slate" style="left:88px;top:22px;width:84px;height:58px"></div>
  <div class="a" style="left:104px;top:28px;width:8px;height:7px;background:#fff;border-radius:4px 4px 0 0"></div>
  <div class="a" style="left:148px;top:28px;width:8px;height:7px;background:#fff"></div>
  <div class="a" style="left:104px;top:54px;width:8px;height:7px;background:#fff;clip-path:polygon(50% 0,100% 50%,50% 100%,0 50%)"></div>
  <div class="a" style="left:148px;top:54px;width:8px;height:7px;background:#fff"></div>
  <div class="a lines-w" style="left:94px;top:38px;width:30px;height:10px"></div>
  <div class="a lines-w" style="left:138px;top:38px;width:30px;height:10px"></div>
  <div class="a lines-w" style="left:94px;top:64px;width:30px;height:10px"></div>
  <div class="a lines-w" style="left:138px;top:64px;width:30px;height:10px"></div>
</div><figcaption class="caption">Slide31.JPG</figcaption></figure>

<figure class="slide-cell"><div class="thumb">
  <div class="tag"></div><div class="mark"></div><div class="t">9 Point Design</div>
  <div class="dot green" style="left:10px;top:28px"></div>
  <div class="dot" style="left:10px;top:46px;background:var(--lime)"></div>
  <div class="dot orange" style="left:10px;top:64px"></div>
  <div class="dot orange" style="left:64px;top:28px"></div>
  <div class="dot slate" style="left:64px;top:46px"></div>
  <div class="dot green" style="left:64px;top:64px"></div>
  <div class="dot pink" style="left:118px;top:28px"></div>
  <div class="dot orange" style="left:118px;top:46px"></div>
  <div class="dot" style="left:118px;top:64px;background:var(--lime)"></div>
  <div class="a lines" style="left:22px;top:26px;width:34px;height:50px"></div>
  <div class="a lines" style="left:76px;top:26px;width:34px;height:50px"></div>
  <div class="a lines" style="left:130px;top:26px;width:34px;height:50px"></div>
</div><figcaption class="caption">Slide32.JPG</figcaption></figure>

<figure class="slide-cell"><div class="thumb">
  <div class="tag"></div><div class="mark"></div><div class="t">Work In Progress</div>
  <div class="photo" role="img" aria-label="Illustration of a standing person" style="left:14px;top:26px;width:16px;height:56px;border-radius:6px;background:linear-gradient(#3a9a46,#3a9a46 55%,#e7a8a0 55%,#e7a8a0)"></div>
  <div class="a" style="left:36px;top:26px;width:8px;height:8px;border-radius:50%;border:1px solid var(--green)"></div>
  <div class="a" style="left:36px;top:40px;width:8px;height:8px;border-radius:50%;border:1px solid var(--green)"></div>
  <div class="a" style="left:36px;top:54px;width:8px;height:8px;border-radius:50%;border:1px solid var(--green)"></div>
  <div class="a" style="left:36px;top:68px;width:8px;height:8px;border-radius:50%;border:1px solid var(--green)"></div>
  <div class="a lines" style="left:48px;top:26px;width:40px;height:50px"></div>
  <div class="a lines" style="left:110px;top:24px;width:40px;height:8px"></div>
  <div class="bars" style="left:106px;top:40px;height:38px">
    <span class="green" style="height:14px"></span><span class="orange" style="height:22px"></span><span style="height:10px;background:#777"></span>
    <span style="width:3px;background:none"></span>
    <span class="green" style="height:18px"></span><span class="orange" style="height:12px"></span><span style="height:20px;background:#777"></span>
    <span style="width:3px;background:none"></span>
    <span class="green" style="height:24px"></span><span class="orange" style="height:16px"></span><span style="height:12px;background:#777"></span>
  </div>
  <div class="a" style="left:104px;top:78px;width:52px;height:1px;background:#aaa"></div>
</div><figcaption class="caption">Slide33.JPG</figcaption></figure>

<figure class="slide-cell"><div class="thumb">
  <div class="tag"></div><div class="mark"></div><div class="t">Branding</div>
  <div class="photo" role="img" aria-label="Illustration of interlocking gears" style="left:12px;top:30px;width:60px;height:46px;border-radius:50%;background:radial-gradient(circle at 35% 40%,#3a9a46 0 30%,#5a5d66 55%,transparent 70%)"></div>
  <div class="a green" style="left:74px;top:30px;width:4px;height:6px"></div>
  <div class="a green" style="left:74px;top:48px;width:4px;height:6px"></div>
  <div class="a slate" style="left:74px;top:66px;width:4px;height:6px"></div>
  <div class="a lines" style="left:82px;top:28px;width:40px;height:50px"></div>
  <div class="a orange" style="left:130px;top:28px;width:32px;height:22px"></div>
  <div class="a orange" style="left:130px;top:56px;width:32px;height:22px"></div>
  <div class="a lines-w" style="left:134px;top:33px;width:24px;height:12px"></div>
  <div class="a lines-w" style="left:134px;top:61px;width:24px;height:12px"></div>
</div><figcaption class="caption">Slide34.JPG</figcaption></figure>

<figure class="slide-cell"><div class="thumb">
  <div class="tag"></div><div class="mark"></div><div class="t">Market Share</div>
  <div class="a lines" style="left:60px;top:22px;width:52px;height:2px"></div>
  <div class="bars" style="left:18px;top:40px;height:30px">
    <span style="height:14px;background:#8dc63f"></span><span class="green" style="height:24px"></span><span class="orange" style="height:10px"></span><span style="height:18px;background:#444"></span>
  </div>
  <div class="bars" style="left:56px;top:40px;height:30px">
    <span style="height:20px;background:#8dc63f"></span><span class="green" style="height:16px"></span><span class="orange" style="height:28px"></span><span style="height:12px;background:#444"></span>
  </div>
  <div class="bars" style="left:94px;top:40px;height:30px">
    <span style="height:10px;background:#8dc63f"></span><span class="green" style="height:26px"></span><span class="orange" style="height:18px"></span><span style="height:22px;background:#444"></span>
  </div>
  <div class="bars" style="left:132px;top:40px;height:30px">
    <span style="height:22px;background:#8dc63f"></span><span class="green" style="height:12px"></span><span class="orange" style="height:16px"></span><span style="height:26px;background:#444"></span>
  </div>
  <div class="a" style="left:12px;top:70px;width:148px;height:1px;background:#aaa"></div>
  <div class="a lines" style="left:14px;top:73px;width:144px;height:8px"></div>
</div><figcaption class="caption">Slide35.JPG</figcaption></figure>

<figure class="slide-cell"><div class="thumb">
  <div class="tag"></div><div class="mark"></div><div class="t">Market Share</div>
  <div class="a green" style="left:12px;top:24px;width:36px;height:7px"></div>
  <div class="a" style="left:48px;top:24px;width:36px;height:7px;background:var(--lime)"></div>
  <div class="a pink" style="left:84px;top:24px;width:38px;height:7px"></div>
  <div class="a slate" style="left:122px;top:24px;width:38px;height:7px"></div>
  <div class="tiny-w" style="left:15px;top:25.5px">FEATURES</div>
  <div class="tiny-w" style="left:51px;top:25.5px">PACKAGE 1</div>
  <div class="tiny-w" style="left:87px;top:25.5px">PACKAGE 2</div>
  <div class="tiny-w" style="left:125px;top:25.5px">PACKAGE 3</div>
  <div class="a" style="left:12px;top:33px;width:148px;height:6px;background:#eee"></div>
  <div class="a" style="left:12px;top:41px;width:148px;height:6px;background:#f6f6f6"></div>
  <div class="a" style="left:12px;top:49px;width:148px;height:6px;background:#eee"></div>
  <div class="a" style="left:12px;top:57px;width:148px;height:6px;background:#f6f6f6"></div>
  <div class="a" style="left:12px;top:65px;width:148px;height:6px;background:#eee"></div>
  <div class="tiny" style="left:15px;top:34.5px">Radio Service</div>
  <div class="tiny" style="left:15px;top:42.5px">Free Hosting</div>
  <div class="tiny" style="left:15px;top:50.5px">Fast Speed</div>
  <div class="tiny" style="left:15px;top:58.5px">Bandwidth Area</div>
  <div class="tiny" style="left:15px;top:66.5px">Hidden Fees</div>
</div><figcaption class="caption">Slide36.JPG</figcaption></figure>

</div>
</main>
</body>
</html>
```